Bluegum Vehicle Hire - The only locally owned company in Central Australia!

We offer 2WD hires
- Small
- Medium
- Large

We offer 4WD hires
- Utes
- Troop Carriers
- Wagons

Servicing Tourism & Mining
Camping packages available
Unlimited kilometer options available

14 Wattle Pde Alice Springs
Contact: 08 8461 3275
www.bluegumvehiclehire.com.au
info@bluegumvehiclehire.com.au

Target Market(s)

Tourism

Industry/Entity Type

Tourism

Contact Information for Business Card

Bluegum Vehicle Hire
The only locally owned company in Central Australia
14 Wattle Parade
Alice Springs NT 0870
Tel: 08 8461 3275
Fax: 08 8467 2914
Miriam Halvorsen
Tobias Halvorsen
We service the tourism industry

Font styles to use
Sans Serif

Colors
0455a3
f37122
9bcb3c

Requirements
Must have
• Name of owners
Nice to have
• Would like to see the company logo appear in green (open to suggestions)
• Pamphlet font information in white. Need a vehicle used to promote our company
Should not have
• should not have any photo's of national icons like Uluru, Kings Canyon

```html
<!DOCTYPE html>
<html lang="en">
<head>
<meta charset="utf-8">
<title>Bluegum Vehicle Hire – Business Card</title>
<link rel="stylesheet" href="https://fonts.googleapis.com/css2?family=Roboto+Condensed:ital,wght@0,400;0,700;1,400&family=Montserrat:wght@400;500&family=Nunito:ital,wght@0,700;0,800;1,800&display=swap">
<style>
  :root {
    --green: #8dc63f;
    --orange: #f37122;
    --navy: #0455a3;
    --ink: #231f20;
    --grey-box: #6d6e71;
    --white: #ffffff;
    --page: #ffffff;
  }
  * { box-sizing: border-box; margin: 0; padding: 0; }
  html, body { width: 1200px; height: 800px; overflow: hidden; background: var(--page); }
  .stage { position: relative; width: 1200px; height: 800px; }

  .card {
    position: absolute; top: 246px; width: 540px; height: 308px;
    overflow: hidden; background: var(--ink);
  }
  .card--front { left: 40px; border-radius: 0 34px 0 34px; }
  .card--back { left: 620px; border-radius: 34px 0 34px 0; }
  .card__bg { position: absolute; inset: 0; }

  /* brand name */
  .brand {
    position: absolute; display: flex; align-items: center; gap: 7px;
    font-family: "Nunito", sans-serif; font-weight: 800; color: var(--white);
    font-size: 17px; line-height: 1.05; letter-spacing: .3px;
  }
  .brand__dot { width: 14px; height: 14px; border-radius: 50%; background: var(--orange); flex: none; }
  .card--front .brand { right: 22px; top: 46px; width: 150px; }
  .card--back .brand { left: 22px; top: 60px; width: 150px; }

  /* front */
  .person { position: absolute; left: 54px; top: 76px; color: var(--white); font-family: "Roboto Condensed", sans-serif; }
  .person__name { font-weight: 700; font-size: 25px; line-height: 1.1; }
  .person__role { font-style: italic; font-size: 17px; margin-top: 2px; }
  .person__mobile { font-size: 23px; margin-top: 4px; }

  .vehicle-photo {
    position: absolute; left: 300px; top: 98px; width: 240px; height: 112px;
    background: linear-gradient(180deg, #7fb2d9 0%, #c6dced 38%, #b8643a 52%, #6e6f72 70%, #3b3b3d 100%);
    -webkit-mask-image: linear-gradient(90deg, transparent 0%, #000 35%);
            mask-image: linear-gradient(90deg, transparent 0%, #000 35%);
  }

  .contacts { position: absolute; left: 36px; top: 194px; list-style: none; color: var(--white); font-family: "Montserrat", sans-serif; font-size: 15px; }
  .contacts li { display: flex; align-items: center; gap: 8px; height: 21.5px; }
  .contacts svg { width: 13px; height: 13px; flex: none; }

  .social { position: absolute; left: 398px; top: 253px; display: flex; gap: 13px; align-items: center; }
  .social__badge { width: 22px; height: 22px; border-radius: 3px; background: var(--navy); }
  .social__badge--warm { background: var(--orange); border-radius: 6px; }
  .social__badge--round { width: 34px; height: 22px; border-radius: 11px; background: var(--white); }

  /* back */
  .camp-photo {
    position: absolute; left: 0; top: 100px; width: 190px; height: 140px;
    background: radial-gradient(ellipse at 55% 65%, #c7a06a 0%, #6d7a8a 35%, #2f3c52 70%, #1d2330 100%);
  }
  .pitch { position: absolute; left: 262px; top: 46px; color: var(--white); font-family: "Nunito", sans-serif; }
  .pitch__head { color: var(--green); font-style: italic; font-weight: 800; font-size: 15.5px; line-height: 14px; }
  .pitch__list { list-style: none; margin-top: 3px; font-weight: 700; font-size: 10.5px; line-height: 13px; }
  .pitch__list li::before { content: "✓"; color: var(--green); margin-right: 4px; font-size: 9px; }

  .fleet { position: absolute; top: 122px; width: 158px; height: 98px; border: 2px solid var(--white); border-radius: 4px; background: var(--grey-box); font-family: "Nunito", sans-serif; color: var(--white); }
  .fleet--2wd { left: 178px; }
  .fleet--4wd { left: 346px; }
  .fleet__title { height: 24px; text-align: center; font-weight: 800; font-size: 19px; line-height: 24px; }
  .fleet--2wd .fleet__title { background: var(--green); }
  .fleet--4wd .fleet__title { background: var(--orange); }
  .fleet__list { list-style: none; padding: 5px 0 0 14px; font-weight: 700; font-size: 14px; line-height: 20px; }
  .fleet--2wd .fleet__list li::before { content: "✓"; color: var(--green); margin-right: 8px; }
  .fleet--4wd .fleet__list li::before { content: "✓"; color: var(--orange); margin-right: 8px; }

  .services { position: absolute; left: 0; top: 240px; width: 540px; height: 27px; background: var(--orange); }
  .service { position: absolute; top: 226px; display: flex; align-items: center; gap: 8px; font-family: "Nunito", sans-serif; font-weight: 700; font-size: 10.5px; line-height: 10px; color: var(--white); }
  .service__icon { width: 48px; height: 48px; border-radius: 50%; background: var(--white); border: 3px solid var(--orange); display: flex; align-items: center; justify-content: center; }
  .service__icon svg { width: 28px; height: 28px; }
  .service--tourism { left: 34px; }
  .service--camping { left: 186px; }
  .service--km { left: 352px; }
</style>
</head>
<body>
<main class="stage">

  <section class="card card--front" aria-label="Business card front">
    <svg class="card__bg" viewBox="0 0 540 308" preserveAspectRatio="none" aria-hidden="true">
      <rect width="540" height="308" fill="var(--green)"/>
      <path d="M0,78 C90,34 210,20 300,40 C330,46 345,30 380,26 L540,20 L540,308 L0,308Z" fill="var(--ink)"/>
      <path d="M0,78 C90,34 210,20 300,40 C330,46 345,30 380,26 L540,20" fill="none" stroke="var(--white)" stroke-width="3"/>
    </svg>
    <div class="vehicle-photo" role="img" aria-label="Two white hire vehicles, a 4WD and an SUV, on an outback road under blue sky"></div>
    <div class="brand"><span class="brand__dot"></span><span>BLUEGUM VEHICLE HIRE</span></div>

    <div class="person">
      <p class="person__name">Tobias Halvorsen</p>
      <p class="person__role">Managing Director</p>
      <p class="person__mobile">04 7302 5186</p>
    </div>

    <ul class="contacts">
      <li><svg viewBox="0 0 12 12"><path d="M6 0.5a4 4 0 0 0-4 4c0 3 4 7 4 7s4-4 4-7a4 4 0 0 0-4-4zm0 5.5a1.5 1.5 0 1 1 0-3 1.5 1.5 0 0 1 0 3z" fill="var(--green)"/></svg>14 Wattle Pde Alice Springs</li>
      <li><svg viewBox="0 0 12 12"><path d="M3 1l2 2.5-1.2 1.3c.6 1.3 1.6 2.4 2.9 3l1.3-1.2L11 8.5 9.6 10.5C5.5 10.2 1.8 6.5 1.5 2.4z" fill="var(--green)"/></svg>08 8461 3275</li>
      <li><svg viewBox="0 0 12 12"><rect x="0.5" y="2.5" width="11" height="7" fill="var(--green)"/><path d="M0.5 2.5 6 6.5l5.5-4" fill="none" stroke="var(--ink)"/></svg>info@bluegumvehiclehire.com.au</li>
      <li><svg viewBox="0 0 12 12"><circle cx="6" cy="6" r="5" fill="none" stroke="var(--green)"/><path d="M1 6h10M6 1c-2.5 3-2.5 7 0 10M6 1c2.5 3 2.5 7 0 10" fill="none" stroke="var(--green)" stroke-width=".8"/></svg>www.bluegumvehiclehire.com.au</li>
    </ul>

    <div class="social" aria-label="Social and listing badges">
      <span class="social__badge"></span>
      <span class="social__badge social__badge--warm"></span>
      <span class="social__badge social__badge--round"></span>
    </div>
  </section>

  <section class="card card--back" aria-label="Business card back">
    <svg class="card__bg" viewBox="0 0 540 308" preserveAspectRatio="none" aria-hidden="true">
      <rect width="540" height="308" fill="var(--green)"/>
      <path d="M0,50 C60,42 150,38 230,32 C330,16 460,18 500,48 C520,64 530,88 540,104 L540,308 L0,308Z" fill="var(--ink)"/>
      <path d="M0,50 C60,42 150,38 230,32 C330,16 460,18 500,48 C520,64 530,88 540,104" fill="none" stroke="var(--white)" stroke-width="3"/>
    </svg>
    <div class="camp-photo" role="img" aria-label="Lit camping tent among desert shrubs at dusk"></div>
    <div class="brand"><span class="brand__dot"></span><span>BLUEGUM VEHICLE HIRE</span></div>

    <div class="pitch">
      <p class="pitch__head">Explore the beauty of the<br>Outback at your own pace</p>
      <ul class="pitch__list">
        <li>Full Camping Kits provide all you need</li>
        <li>Sleep Under the Stars in a Swag</li>
        <li>Stay at the most beautiful spots</li>
      </ul>
    </div>

    <div class="fleet fleet--2wd">
      <h2 class="fleet__title">2WD Hires</h2>
      <ul class="fleet__list"><li>Small</li><li>Medium</li><li>Large</li></ul>
    </div>
    <div class="fleet fleet--4wd">
      <h2 class="fleet__title">4WD Hires</h2>
      <ul class="fleet__list"><li>Utes</li><li>Troop Carriers</li><li>Wagons</li></ul>
    </div>

    <div class="services"></div>
    <div class="service service--tourism">
      <span class="service__icon"><svg viewBox="0 0 28 28"><rect x="6" y="9" width="10" height="14" rx="2" fill="var(--ink)"/><path d="M9 9V5h4v4M18 22l5-9M20 13h5" stroke="var(--ink)" stroke-width="2" fill="none"/></svg></span>
      <span>Servicing Tourism<br>&amp; Mining</span>
    </div>
    <div class="service service--camping">
      <span class="service__icon"><svg viewBox="0 0 28 28"><path d="M2 22 12 6l14 16z" fill="var(--ink)"/><path d="M12 22l3-7 3 7z" fill="var(--white)"/></svg></span>
      <span>Camping Packages</span>
    </div>
    <div class="service service--km">
      <span class="service__icon"><svg viewBox="0 0 28 28"><path d="M3 19a11 11 0 1 1 22 0" fill="none" stroke="var(--ink)" stroke-width="2.5"/><path d="M14 19l5-7" stroke="var(--ink)" stroke-width="2"/><circle cx="14" cy="19" r="2" fill="var(--ink)"/></svg></span>
      <span>Unlimited Kilometer<br>Options</span>
    </div>
  </section>

</main>
</body>
</html>
```